VMR business card

Need a business card for a company that provides instructional design and elearning development services. The website is here: http://vantmoro.studio/

I'm attaching a current logo, as well as the old business card design. While I like to keep it clean, the old design is too simplistic for my liking. The only idea I want to reuse from the old design is placing industry jargon on the back of the card, just need a better way to present it. But if you have other ideas for the back--feel free to experiment.

Please use the colors complementary to the color we have on the website. Thank you!

```html
<!DOCTYPE html>
<html lang="en">
<head>
<meta charset="utf-8">
<title>VMR Business Card</title>
<link rel="stylesheet" href="https://fonts.googleapis.com/css2?family=Lato:wght@300;400;700;900&family=Open+Sans:wght@400;600&family=Montserrat:wght@700&display=swap">
<style>
  :root {
    --backdrop: #dccb8f;
    --card-white: #ffffff;
    --card-cream: #f3efdd;
    --teal: #14a8a0;
    --charcoal: #454545;
    --gold: #d9c98a;
    --ink: #4a4a4a;
    --muted: #8a8a8a;
  }
  * { margin: 0; padding: 0; box-sizing: border-box; }
  html, body {
    width: 1200px; height: 800px; overflow: hidden;
    background: var(--backdrop);
  }
  .stage {
    position: relative; width: 1200px; height: 800px;
    display: flex; align-items: center; justify-content: center; gap: 60px;
  }
  .card {
    position: relative; width: 500px; height: 286px; overflow: hidden;
    box-shadow: 0 6px 14px rgba(0,0,0,0.18);
  }

  /* Front */
  .card-front { background: var(--card-white); }
  .card-front .edge-shapes { position: absolute; inset: 0; }
  .front-content {
    position: absolute; left: 150px; top: 78px;
    font-family: "Open Sans", sans-serif;
  }
  .brand {
    display: flex; align-items: center; gap: 10px;
    margin-bottom: 16px;
  }
  .brand-mark { width: 22px; height: 22px; background: var(--teal); }
  .brand-name {
    font-family: "Lato", sans-serif; font-weight: 900;
    font-size: 38px; letter-spacing: 2px; color: var(--teal); line-height: 1;
  }
  .person-name {
    font-family: "Montserrat", sans-serif; font-weight: 700;
    font-size: 19px; color: var(--ink); margin-bottom: 12px;
  }
  .contact { list-style: none; font-size: 11.5px; color: var(--muted); line-height: 1.65; padding-left: 40px; }

  /* Back */
  .card-back { background: var(--charcoal); }
  .question {
    position: absolute; left: 26px; top: 100px;
    font-family: "Lato", sans-serif; color: var(--teal);
    font-size: 30px; line-height: 1.05; letter-spacing: 1px;
  }
  .question span { display: block; font-weight: 300; }
  .question .q-step-1 { margin-left: 0; }
  .question .q-step-2 { margin-left: 30px; }
  .question .q-step-3 { margin-left: 62px; }
  .question .q-step-4 { margin-left: 84px; font-weight: 900; }
  .jargon {
    position: absolute; left: 170px; top: 42px;
    font-family: "Lato", sans-serif; color: var(--gold);
    list-style: none; line-height: 1.45;
  }
  .jargon li { white-space: nowrap; }
  .jargon .light { font-weight: 300; font-size: 15px; letter-spacing: 1.5px; }
  .jargon .bold { font-weight: 900; font-size: 16px; letter-spacing: 0.5px; }
  .jargon .l1 { margin-left: 20px; }
  .jargon .l2 { margin-left: 4px; }
  .jargon .l3 { margin-left: 26px; }
  .jargon .l4 { margin-left: 24px; }
  .jargon .l5 { margin-left: 38px; }
  .jargon .l6 { margin-left: 54px; }
</style>
</head>
<body>
<main class="stage">
  <section class="card card-front" aria-label="Business card front">
    <svg class="edge-shapes" viewBox="0 0 500 286" width="500" height="286" aria-hidden="true">
      <polygon points="0,0 55,0 0,120" fill="var(--card-cream)"/>
      <polygon points="430,0 500,0 500,58" fill="var(--teal)"/>
    </svg>
    <div class="front-content">
      <div class="brand">
        <span class="brand-mark" aria-hidden="true"></span>
        <span class="brand-name">VMR</span>
      </div>
      <h1 class="person-name">Marcus Delaney</h1>
      <ul class="contact">
        <li>555-013-2748</li>
        <li>mdelaney@vantmoro.studio</li>
        <li>www.vantmoro.studio</li>
      </ul>
    </div>
  </section>

  <section class="card card-back" aria-label="Business card back">
    <p class="question">
      <span class="q-step-1">HOW</span>
      <span class="q-step-2">CAN</span>
      <span class="q-step-3">WE</span>
      <span class="q-step-4">HELP?</span>
    </p>
    <ul class="jargon">
      <li class="light l1">MOBILE LEARNING SCORM</li>
      <li class="bold l2">INSTRUCTIONAL DESIGN LMS</li>
      <li class="light l3">MOOCS ELEARNING HTML5</li>
      <li class="bold l4">ADULT LEARNING THEORY</li>
      <li class="light l5">GAMIFICATION CLASSROOM</li>
      <li class="bold l6">XAPI BLENDED LEARNING</li>
    </ul>
  </section>
</main>
</body>
</html>
```